Personal Business Card

Looking for a clean and modern personal business card. Basically I need something catchy to give to potential clients and people I meet. I do a lot of freelancing (from DJ'ing to wedding videography, but its mostly on the event side of things) so it's more-so about selling myself rather than identifying with a company. I'm starting to meet more people that I want to work with after meeting them so I'm revamping my business cards.

I'm looking for a clean and modern design- I know that's really vague but I'm fine with anything ranging from a symbol to just a fancy version of my name.

Details I need on the front:
Dennis Kowal
dennis@denniskowal-mail.net
(555) 807-2291

On the back I'd like to have something simple like "Nice to have met you today" or "Great meeting you".

UPDATE 9/27 Noon: My apologies for not putting it up before- I'm definitely looking for full color. Doesn't have to be a rainbow but I am looking for the least amount of blank white as possible.

UPDATE 10/1: Really impressed with what I've been getting so far and I'm working on giving everyone feedback- if your design is still up then you're still in the run. Looking for something more unique and modern so please do not post something that looks like a template from Cardloom!

Target Market(s)

Mainly to give to people aged 18-35. Most of my encounters will be casual so the card should have a "young" feeling to it. I rarely do anything in the corporate world so it doesn't have to be boring. It should give the impression that I'm the one they should go to if they need what I do (again it changes every weekend so I'll probably say the "what I do" part.

Industry/Entity Type

Wedding

Requirements
Must have
• Basically the contact information listed above
Nice to have
• I really like the colors Blue, Silver, and Purple. They don't have to necessarily all be there though. I do like the look of polished metal if that makes sense.
Should not have
• A template that resembles card-loom. I'm in a point in my life where I'm working a lot of different markets/areas so the card does not need to have an address or address placeholder.

```html
<!DOCTYPE html>
<html lang="en">
<head>
<meta charset="utf-8">
<title>Dennis Kowal — Business Card</title>
<link rel="stylesheet" href="https://fonts.googleapis.com/css2?family=Exo+2:wght@600&family=Questrial&display=swap">
<style>
  :root {
    --page: #fdfdfd;
    --card-dark: #1f1e1e;
    --card-glow: #2c2b2a;
    --accent: #f5883a;
    --ink-light: #ffffff;
    --ink-soft: #e6e6e6;
  }
  * { margin: 0; padding: 0; box-sizing: border-box; }
  html, body {
    width: 1200px;
    height: 1066px;
    overflow: hidden;
    background: var(--page);
  }
  .canvas {
    position: relative;
    width: 1200px;
    height: 1066px;
  }
  .card {
    position: absolute;
    width: 848px;
    height: 401px;
    border-radius: 20px;
    overflow: hidden;
    background: radial-gradient(ellipse 60% 70% at 45% 45%, var(--card-glow) 0%, var(--card-dark) 75%);
  }
  .card--front { left: 179px; top: 117px; }
  .card--back  { left: 173px; top: 550px; }
  .card__band {
    position: absolute;
    top: 0;
    right: 0;
    width: 57px;
    height: 100%;
    background: var(--accent);
  }
  .monogram-area {
    position: absolute;
    left: 81px;
    top: 0;
    width: 156px;
    height: 223px;
    background: var(--accent);
  }
  .identity {
    position: absolute;
    left: 21px;
    top: 231px;
  }
  .identity__name {
    font-family: "Exo 2", sans-serif;
    font-weight: 600;
    font-size: 28px;
    line-height: 1;
    letter-spacing: 0.5px;
    text-transform: uppercase;
    white-space: nowrap;
  }
  .identity__first { color: var(--accent); }
  .identity__last  { color: var(--ink-light); }
  .contact {
    font-family: "Questrial", sans-serif;
    font-size: 13.5px;
    color: var(--ink-soft);
    line-height: 1.4;
  }
  .contact--web { margin-top: 4px; }
  .contact-list { margin-top: 38px; }
  .greeting {
    position: absolute;
    left: 0;
    right: 57px;
    top: 234px;
    text-align: center;
    font-family: "Exo 2", sans-serif;
    font-weight: 600;
    font-size: 27px;
    line-height: 1;
    text-transform: uppercase;
    letter-spacing: 0.5px;
    white-space: nowrap;
  }
  .greeting__lead { color: var(--accent); }
  .greeting__end  { color: var(--ink-light); }
</style>
</head>
<body>
<main class="canvas">
  <section class="card card--front" aria-label="Card front">
    <div class="monogram-area" role="img" aria-label="Large personal initial monogram"></div>
    <div class="identity">
      <h1 class="identity__name"><span class="identity__first">Dennis</span> <span class="identity__last">Kowal</span></h1>
      <p class="contact contact--web">http://www.denniskowal-site.net</p>
      <div class="contact-list">
        <p class="contact">(555) 807-2291</p>
        <p class="contact">dennis@denniskowal-mail.net</p>
      </div>
    </div>
    <div class="card__band"></div>
  </section>

  <section class="card card--back" aria-label="Card back">
    <p class="greeting"><span class="greeting__lead">Great Meeting</span> <span class="greeting__end">You...</span></p>
    <div class="card__band"></div>
  </section>
</main>
</body>
</html>
```